Marketing Flyer

I need a flyer for my marketing company. I would like for it to to be consistent with my logo and business card design. I would also like for there to be an image of a crowded waiting room, or restaurant with people gathered around a flat screen that reads "Your Ad Here".

Requirements
Must have
• logo, info on attached doc.
Nice to have
• Possibly a picture people in a waiting room or restaurant with a digital sign present that reads "your ad here".

```html
<!DOCTYPE html>
<html lang="en">
<head>
<meta charset="utf-8">
<title>FieldLine Marketing Flyer</title>
<link href="https://fonts.googleapis.com/css2?family=Figtree:wght@400;500;600;700;800&display=swap" rel="stylesheet">
<style>
  :root {
    --green: #8cc63f;
    --gray-dark: #5e5e5e;
    --gray-text: #6b6b6b;
    --ink: #2b2b2b;
    --paper: #ffffff;
    --stage: #eceeee;
    --screen: #5a5a5a;
    --screen-text: #eef3df;
  }
  * { box-sizing: border-box; margin: 0; padding: 0; }
  html, body { width: 1200px; height: 1200px; overflow: hidden; }
  body {
    background: var(--stage);
    font-family: "Figtree", sans-serif;
    position: relative;
  }
  .flyer {
    position: absolute;
    left: 168px; top: 31px;
    width: 863px; height: 1137px;
    background: var(--paper);
    box-shadow: 0 6px 24px rgba(0,0,0,0.18);
    overflow: hidden;
  }
  .brand { position: absolute; left: 30px; top: 16px; color: var(--gray-dark); }
  .brand-name { font-size: 92px; font-weight: 700; line-height: 1; letter-spacing: -2px; }
  .brand-sub { font-size: 26px; font-weight: 400; letter-spacing: 15px; margin-top: 4px; }
  .contact { position: absolute; left: 586px; top: 26px; width: 210px; }
  .contact-title { font-size: 29px; font-weight: 700; color: var(--gray-text); padding-bottom: 8px; border-bottom: 2px solid var(--green); }
  .contact-line { display: flex; align-items: center; gap: 6px; font-size: 15px; color: var(--gray-text); margin-top: 8px; white-space: nowrap; }
  .contact-line svg { width: 14px; height: 14px; flex: none; }
  .hero {
    position: absolute; left: 3px; top: 149px; width: 860px; height: 516px;
    background: linear-gradient(180deg, #8a4a3e 0%, #7a443a 45%, #3c2e2c 75%, #2a2626 100%);
  }
  .hero-screen {
    position: absolute; left: 193px; top: 23px; width: 383px; height: 219px;
    background: var(--screen); border: 5px solid #1e1e1e;
    text-align: center; overflow: hidden;
  }
  .hero-screen-text { color: var(--screen-text); font-size: 60px; font-weight: 700; line-height: 0.98; margin-top: 14px; }
  .hero-headline {
    position: absolute; left: 0; right: 0; top: 360px;
    text-align: center; color: #fff; font-size: 62px; font-weight: 800; line-height: 1.02;
  }
  .benefits-title {
    position: absolute; left: 0; right: 0; top: 672px; text-align: center;
    font-size: 45px; font-weight: 700; color: var(--green);
  }
  .benefits-rule { position: absolute; left: 36px; top: 741px; width: 798px; height: 3px; background: var(--green); }
  .service-tag {
    position: absolute; left: 14px; top: 768px; width: 254px; height: 47px;
    background: var(--gray-dark);
    clip-path: polygon(0 0, 100% 0, 94% 100%, 0 100%);
    color: var(--green); font-weight: 700; font-size: 26px;
    display: flex; align-items: center; padding-left: 37px;
  }
  .service-lead {
    position: absolute; left: 297px; top: 752px; width: 540px;
    font-size: 28px; font-weight: 600; color: var(--gray-text); line-height: 1.2;
  }
  .benefit-list { position: absolute; left: 34px; top: 840px; width: 790px; list-style: none; }
  .benefit-list li {
    position: relative; padding-left: 20px;
    font-size: 16px; line-height: 23.6px; color: var(--ink);
  }
  .benefit-list li::before {
    content: ""; position: absolute; left: 0; top: 7px; width: 10px; height: 12px;
    background: var(--green); border-radius: 0 100% 0 100%;
  }
  .footer-band { position: absolute; left: 0; bottom: 0; width: 100%; height: 26px; background: var(--green); }
</style>
</head>
<body>
  <div class="flyer">
    <div class="brand">
      <div class="brand-name">FieldLine</div>
      <div class="brand-sub">MARKETING</div>
    </div>

    <div class="contact">
      <div class="contact-title">Contact us</div>
      <div class="contact-line">
        <svg viewBox="0 0 24 24"><path fill="#8cc63f" d="M6.6 10.8a15 15 0 0 0 6.6 6.6l2.2-2.2a1 1 0 0 1 1-.25 11.4 11.4 0 0 0 3.6.57 1 1 0 0 1 1 1V20a1 1 0 0 1-1 1A17 17 0 0 1 3 4a1 1 0 0 1 1-1h3.5a1 1 0 0 1 1 1c0 1.25.2 2.45.57 3.57a1 1 0 0 1-.25 1z"/></svg>
        +555-0142-88
      </div>
      <div class="contact-line">
        <svg viewBox="0 0 24 24"><path fill="#8cc63f" d="M2 5h20v14H2z"/><path fill="none" stroke="#fff" stroke-width="2" d="M2 5l10 8 10-8"/></svg>
        hello@fieldline-media.com
      </div>
    </div>

    <div class="hero" role="img" aria-label="Photo of a crowded sports bar with a brick wall, people cheering in front of wall-mounted TV screens">
      <div class="hero-screen">
        <div class="hero-screen-text">YOUR AD<br>HERE</div>
      </div>
      <div class="hero-headline">Let us make you famous<br>in your community!</div>
    </div>

    <h2 class="benefits-title">Benefits of Advertising with FieldLine</h2>
    <div class="benefits-rule"></div>

    <div class="service-tag">WHAT WE DO</div>
    <p class="service-lead">We design an ad for your company and place it on the TV at local businesses.</p>

    <ul class="benefit-list">
      <li>Inexpensive: Only $31.00 per month!</li>
      <li>Exposure: Our digital signage is placed in only the best/high traffic businesses in your area.</li>
      <li>Repetition: Your ad is shown over 3,500 time each month (42,000 times per year)!</li>
      <li>Local: We show your ad to consumers in YOUR area. Let us help you do business with the people you want to do business with.</li>
      <li>Exclusivity: Only 2 ads per industry.</li>
      <li>Location: We show consumers how to reach you and where to find you.</li>
      <li>Awareness: People need to know your business. We make that happen by putting your brand right in front of them.</li>
      <li>Digital: Digital advertising has higher retention rates and higher consumer engagement.</li>
    </ul>

    <div class="footer-band"></div>
  </div>
</body>
</html>
```